IT Network Consultancy - Business Card

t4 linkways is a IT network consultancy based in London. We're looking for a smart, modern and professional business card design. Our website is here: www.t4linkways.co.uk

Key things that should be included on the card (with examples):

Company Logo
Name
Position / Job Title: Network Consultant
Mobile Phone Number: +44 (0) 7700 900418
Land Line: +44 (0) 1632 960274
Email Address: name@t4linkways.co.uk
Web Site URL: www.t4linkways.co.uk

Target Market(s)

Large enterprise / global companies / corporates

Industry/Entity Type

Business

Requirements
Must have
• Incorporate our logo - which is attached to the project. They are in AI format (can be opened in Inkscape).

The design should be double sided and fit on a UK standard 85mm × 55mm card and be in a format that retains the quality when printed.
Nice to have
• The project does not have to conform to the colour of our website but this should give you inspiration of the style we like.
Should not have
• Bright colours. Pictures are not necessary.

```html
<!DOCTYPE html>
<html lang="en">
<head>
<meta charset="utf-8">
<title>t4 linkways – Business Card</title>
<link href="https://fonts.googleapis.com/css2?family=Nunito:wght@400;800&family=Tinos:ital,wght@0,700;1,700&display=swap" rel="stylesheet">
<style>
  :root {
    --page: #ffffff;
    --notch: #eef4fb;
    --silver-light: #f4f5f6;
    --silver-mid: #d9dbde;
    --silver-dark: #b9bcc1;
    --card-edge: #c9ccd0;
    --logo: #4f5964;
    --detail: #8b9097;
    --label: #111111;
    --link: #2b3a9c;
    --caption: #222222;
    --ghost: rgba(255, 255, 255, 0.35);
  }
  html, body {
    margin: 0;
    padding: 0;
    width: 1200px;
    height: 2203px;
    overflow: hidden;
    background: var(--page);
  }
  .canvas {
    position: relative;
    width: 1200px;
    height: 2203px;
  }
  .card {
    position: absolute;
    left: 214px;
    width: 791px;
    height: 517px;
    border-radius: 40px;
    overflow: hidden;
    background:
      radial-gradient(ellipse at 70% 20%, rgba(255,255,255,0.7), rgba(255,255,255,0) 55%),
      linear-gradient(100deg, var(--silver-dark) 0%, var(--silver-light) 30%, var(--silver-mid) 55%, var(--silver-light) 75%, var(--silver-dark) 100%);
    box-shadow: inset 0 0 0 2px var(--card-edge);
  }
  .card--front { top: 231px; }
  .card--back { top: 1319px; }
  .notch {
    position: absolute;
    width: 146px;
    height: 146px;
    border-radius: 50%;
    background: var(--notch);
  }
  .wordmark {
    position: absolute;
    margin: 0;
    font-family: "Nunito", sans-serif;
    font-weight: 400;
    font-size: 58px;
    line-height: 1;
    color: var(--logo);
    white-space: nowrap;
  }
  .card--front .wordmark { right: 58px; top: 58px; }
  .card--back .wordmark { left: 0; right: 0; top: 188px; text-align: center; }
  .ghost-mark {
    position: absolute;
    left: 0;
    right: 0;
    text-align: center;
    font-family: "Nunito", sans-serif;
    font-weight: 400;
    font-size: 120px;
    line-height: 1;
    color: var(--ghost);
    white-space: nowrap;
  }
  .card--front .ghost-mark { top: 330px; }
  .card--back .ghost-mark { top: 320px; }
  .contact {
    position: absolute;
    left: 0;
    right: 0;
    top: 256px;
    margin: 0;
    text-align: center;
    font-family: "Nunito", sans-serif;
    font-weight: 800;
    font-size: 29px;
    line-height: 41px;
    color: var(--detail);
  }
  .web-details {
    position: absolute;
    left: 0;
    right: 0;
    top: 276px;
    margin: 0;
    text-align: center;
    font-family: "Tinos", serif;
    font-size: 26px;
    line-height: 33px;
  }
  .web-details .label { font-weight: 700; color: var(--label); }
  .web-details .value { font-weight: 700; font-style: italic; color: var(--link); }
  .caption {
    position: absolute;
    left: 0;
    width: 1200px;
    margin: 0;
    text-align: center;
    font-family: Arial, "Helvetica", sans-serif;
    font-size: 38px;
    color: var(--caption);
  }
  .caption--front { top: 785px; }
  .caption--back { top: 1899px; }
</style>
</head>
<body>
<main class="canvas">
  <section class="card card--front" aria-label="Card front">
    <div class="ghost-mark" aria-hidden="true">t4 linkways</div>
    <p class="wordmark">t4 linkways</p>
    <p class="contact">
      Daniel<br>
      Network Consultant<br>
      +44 (0) 7700 900418<br>
      Land Line: +44 (0) 1632 960274
    </p>
  </section>
  <div class="notch" style="left:131px; top:415px;"></div>
  <div class="notch" style="left:932px; top:415px;"></div>
  <p class="caption caption--front">Front</p>

  <section class="card card--back" aria-label="Card back">
    <div class="ghost-mark" aria-hidden="true">t4 linkways</div>
    <p class="wordmark">t4 linkways</p>
    <p class="web-details">
      <span class="label">Email Address:</span> <span class="value">name@t4linkways.co.uk</span><br>
      <span class="label">Web Site URL:</span> <span class="value">www.t4linkways.co.uk"</span><br>
      <span class="value">rel="nofollow"&gt;www.t4linkways.co.uk</span>
    </p>
  </section>
  <div class="notch" style="left:131px; top:1503px;"></div>
  <div class="notch" style="left:932px; top:1503px;"></div>
  <p class="caption caption--back">Back</p>
</main>
</body>
</html>
```